Boutique Film/TV Company needs Business Card Design

Please see our website for background on our company and look of our current logo: www.morlandpictures.ca

Pantone 314U is our main colour.

Target Market(s)

Network of peers, funders and broadcasters.

Industry/Entity Type

Business

Requirements
Must have
• We would like rounded corners and the height of the card to be shorter than traditional (maybe?!)

It's important that we have room for our office address, office number, cell number, email address, website, facebook and linked-in info (though not all of us have a linked-in account).

Would like the logo to keep the exclamation marks over the letters but the tag line/tag words of "film - television - interactive" can stay or go or... surprise me!

Nice to have
• Silky matte finish.

We are open to a change in the font of our logo/name.

```html
<!DOCTYPE html>
<html lang="en">
<head>
<meta charset="utf-8">
<title>Morland Pictures — Business Card</title>
<link rel="stylesheet" href="https://fonts.googleapis.com/css2?family=Jost:wght@400;500;600&family=Open+Sans:wght@700&display=swap">
<style>
  :root {
    --stage: #3a3a3a;
    --stage-edge: #262626;
    --card-glow: #00e6ef;
    --card-mid: #0bb3d6;
    --card-edge: #0a6fab;
    --tagword: rgba(160, 235, 245, 0.28);
    --white: #ffffff;
    --ink: #07182a;
    --rule: rgba(255, 255, 255, 0.85);
  }
  * { box-sizing: border-box; margin: 0; padding: 0; }
  html, body { width: 1200px; height: 785px; overflow: hidden; }
  body {
    background: radial-gradient(ellipse at 50% 45%, var(--stage) 0%, var(--stage-edge) 80%);
    font-family: "Jost", "Futura", sans-serif;
    position: relative;
  }
  .card {
    position: absolute;
    border-radius: 26px;
    overflow: hidden;
    box-shadow: 0 6px 12px rgba(0, 0, 0, 0.45);
  }
  .card--front {
    left: 116px; top: 246px; width: 473px; height: 287px;
    background: radial-gradient(ellipse 62% 70% at 47% 50%, var(--card-glow) 0%, var(--card-mid) 50%, var(--card-edge) 100%);
  }
  .card--back {
    left: 617px; top: 245px; width: 484px; height: 286px;
    background: radial-gradient(ellipse 60% 72% at 46% 32%, var(--card-glow) 0%, var(--card-mid) 52%, var(--card-edge) 100%);
  }
  .tagword {
    position: absolute;
    font-family: "Open Sans", Arial, sans-serif;
    font-weight: 700;
    color: var(--tagword);
    line-height: 1;
    white-space: nowrap;
  }
  .tagword--tv { font-size: 44px; }
  .tagword--film { font-size: 33px; }
  .tagword--interactive { font-size: 54px; }
  .card--front .tagword--tv { left: 75px; top: 30px; }
  .card--front .tagword--film { left: 21px; top: 76px; }
  .card--front .tagword--interactive { left: 122px; top: 94px; }
  .card--back .tagword--tv { left: 121px; top: 42px; }
  .card--back .tagword--film { left: 68px; top: 84px; }
  .card--back .tagword--interactive { left: 166px; top: 98px; }
  .brand-name {
    position: absolute;
    color: var(--white);
    font-weight: 400;
    line-height: 1;
    white-space: nowrap;
  }
  .card--front .brand-name { right: 26px; top: 196px; font-size: 62px; }
  .card--back .brand-name { right: 30px; top: 24px; font-size: 42px; }
  .person-name {
    position: absolute; left: 37px; top: 142px;
    color: var(--white); font-size: 19px; font-weight: 500; letter-spacing: 0.5px;
  }
  .person-title {
    position: absolute; left: 37px; top: 163px;
    color: var(--ink); font-size: 12px; font-variant: small-caps; letter-spacing: 0.2px;
  }
  .divider {
    position: absolute; left: 37px; top: 178px; width: 419px; height: 1px;
    background: var(--rule);
  }
  .contact-list {
    position: absolute; left: 38px; top: 186px; list-style: none;
  }
  .contact-list li {
    display: flex; align-items: center; height: 15.5px;
    color: var(--ink); font-size: 13px; font-variant: small-caps; letter-spacing: 0.3px;
  }
  .contact-list svg { width: 11px; height: 11px; margin-right: 9px; flex: none; fill: var(--white); }
</style>
</head>
<body>
  <section class="card card--front">
    <span class="tagword tagword--tv">Television</span>
    <span class="tagword tagword--film">Film</span>
    <span class="tagword tagword--interactive">Interactive</span>
    <span class="brand-name">Morland</span>
  </section>

  <section class="card card--back">
    <span class="brand-name">Morland</span>
    <span class="tagword tagword--tv">Television</span>
    <span class="tagword tagword--film">Film</span>
    <span class="tagword tagword--interactive">Interactive</span>
    <h1 class="person-name">DANIEL HARTLEY</h1>
    <p class="person-title">Head of Development, Drama and Scripted Content</p>
    <div class="divider"></div>
    <ul class="contact-list">
      <li><svg viewBox="0 0 12 12"><path d="M6 1 L11.5 6 H10 V11 H7 V8 H5 V11 H2 V6 H0.5 Z"/></svg>48 Linden Avenue, Toronto, ON&nbsp; M4K 2B7</li>
      <li><svg viewBox="0 0 12 12"><path d="M2.5 1 L4.5 1 L5.2 3.5 L4 4.5 Q5 7 7.5 8 L8.5 6.8 L11 7.5 L11 9.5 Q10 11 8 10.8 Q2 9.5 1 3.5 Q1 1.8 2.5 1 Z"/></svg>+ 416.555.0187</li>
      <li><svg viewBox="0 0 12 12"><rect x="3" y="1" width="6" height="10.5" rx="1"/><rect x="4.2" y="2.5" width="3.6" height="3.5" fill="#0bb3d6"/></svg>+ 416.555.0142</li>
      <li><svg viewBox="0 0 12 12"><path d="M1 5 L6 1.5 L11 5 V10.5 H1 Z"/><path d="M1.5 5.3 L6 8.3 L10.5 5.3" stroke="#0bb3d6" stroke-width="0.9" fill="none"/></svg>info@morlandpictures.ca</li>
      <li><svg viewBox="0 0 12 12"><circle cx="6" cy="6" r="5" fill="none" stroke="#fff" stroke-width="1"/><path d="M1 6 H11 M6 1 V11 M6 1 Q2.5 6 6 11 M6 1 Q9.5 6 6 11" stroke="#fff" stroke-width="0.8" fill="none"/></svg>www.morlandpictures.ca</li>
    </ul>
  </section>
</body>
</html>
```